MailCraft newsletter template & Facebook / LinkedIn header design for BELMOR group

Hi all,
We are BELMOR: a company providing technology solutions to the construction industry. We have a brand new website - www.belmorsolutions.com - and are looking for a MailCraft Newsletter Template that matches our new website design. In addition, we are looking for a Facebook and LinkedIn header in line with our new website and news letter template.
Our company is located in 4 countries. Please visit our website for more information about our company:
The Netherlands - www.belmorsolutions.nl
Denmark - www.belmorsolutions.dk
Sweden - www.belmorsolutions.se
Norway - www.belmorsolutions.no
An English translation can be accessed via www.belmorsolutions.com.
Look and Feel:
In line with our website (please refer to links above)
Match the high-tech, innovative, fresh character of our company BELMOR
Keywords: clean / simple / robust

Updates
Project Deadline Extended
Reason: Due to the holidayweekend, we weren't able to provide all designers sufficient and equal feedback. Therefore we have delayed the deadline with three days.

Target Market(s)
Building / construction companies in Northern Europe.
Industry/Entity Type
Construction
Colors
Designer to choose colors to be used in the design.
Requirements
Must have
- Requirements for News letter template:
Use of our BELMOR logo (attached)
Use of BELMOR grid in line with our website (attached)
Use of the BELMOR colours
Links to Social Media
Room for promotions
Room for upcoming events
Promotion of our new website www.belmorsolutions.com
To be used for email and PDF
Requirements for Facebook / LinkedIn:
Use of the BELMOR colours
Should not have
- A lot of small details. complicated design.

```html
<!DOCTYPE html>
<html lang="en">
<head>
<meta charset="utf-8">
<title>BELMOR Newsletter Template</title>
<link href="https://fonts.googleapis.com/css2?family=Open+Sans:wght@400;600;700&display=swap" rel="stylesheet">
<style>
:root{
  --stage:#444446;
  --orange:#f5ac3c;
  --orange-deep:#d98f22;
  --navy:#0f4a7d;
  --heading:#1d5f93;
  --ink:#3a3a3a;
  --white:#ffffff;
  --paper:#f6f6f6;
  --gallery:#3d3d3f;
  --photo-a:#c9892e;
  --photo-b:#8a6a3d;
}
*{box-sizing:border-box;margin:0;padding:0}
html,body{width:1132px;height:1200px;overflow:hidden}
body{background:var(--stage);font-family:"Open Sans",Arial,sans-serif;color:var(--ink);position:relative}
.column{position:absolute;top:0;width:231px;height:1200px;overflow:hidden;background:var(--orange)}
.col-1{left:48px}.col-2{left:315px}.col-3{left:586px}.col-4{left:857px}
.block{position:absolute;left:0;width:100%;text-align:center}
h2{font-weight:400;font-size:11px;letter-spacing:.3px;color:var(--heading);text-transform:uppercase}
p{font-size:8.6px;line-height:14.6px;padding:0 22px}
.read-more{display:block;font-size:8.6px;color:var(--heading);text-decoration:underline;margin-top:1px}
.btn{display:inline-block;background:var(--navy);color:var(--white);font-size:6.5px;font-weight:600;letter-spacing:.4px;padding:6px 12px;border-radius:1px;text-transform:uppercase}
.icon{width:52px;height:52px;border:1.6px solid var(--ink);border-radius:50%;background:var(--white);margin:0 auto 14px;display:flex;align-items:center;justify-content:center}
.feature h2{margin-bottom:8px}
.feature p{margin-bottom:14px}
.photo{position:absolute;background:linear-gradient(160deg,var(--photo-a),var(--photo-b))}
.logo-band{height:83px;background:var(--white);display:flex;align-items:center;justify-content:center}
.wordmark{font-weight:700;font-size:24px;color:var(--navy);letter-spacing:.5px}
.hero-title{position:absolute;left:14px;top:75px;background:var(--white);padding:2px 8px 0;font-size:17px;line-height:17px;color:var(--ink);letter-spacing:.4px}
.hero-sub{position:absolute;left:16px;top:118px;color:var(--white);font-size:11px;line-height:13px;width:200px}
.white-panel{background:var(--white)}
.dark-panel{background:var(--gallery)}
.dark-panel h2{color:var(--orange)}
.dark-panel p{color:var(--white)}
.subscribe h2{font-size:10px;color:var(--navy);font-weight:600}
.subscribe-form{display:flex;margin:0 10px}
.subscribe-form .field{flex:1;border:1px solid #ccc;font-size:6.5px;color:#999;text-align:left;padding:8px 7px}
.subscribe-form .submit{background:var(--navy);color:var(--white);font-size:6.5px;font-weight:700;padding:8px 10px}
.video-card{position:absolute;left:10px;width:211px;background:var(--white);border-radius:4px;text-align:center}
.video-card h2{font-size:13px;color:var(--heading)}
.footer{background:var(--navy);color:var(--white)}
.footer .tagline{font-size:10.5px;letter-spacing:2.4px;line-height:16px;text-transform:uppercase}
.rule{height:1px;background:rgba(255,255,255,.45)}
.socials{display:grid;grid-template-columns:repeat(3,20px);gap:13px 20px;justify-content:center}
.social{width:20px;height:20px;border-radius:50%;background:var(--white)}
.footer small{font-size:7.5px}
.footer-links{display:flex;justify-content:space-between;padding:0 18px;font-size:7.5px}
</style>
</head>
<body>

<!-- Column 1 -->
<section class="column col-1">
  <div class="logo-band"><span class="wordmark">BELMOR</span></div>
  <div class="photo" style="top:83px;left:0;width:231px;height:247px" role="img" aria-label="Construction site photo tinted orange, surveyor with equipment">
    <div class="hero-title">MAILCRAFT<br>NEWSLETTER</div>
    <div class="hero-sub">Sed ut perspiciatis unde omnis iste natus error sit voluptatem</div>
  </div>
  <div class="block feature" style="top:352px">
    <div class="icon"><svg width="24" height="24" viewBox="0 0 24 24" fill="none" stroke="#3a3a3a" stroke-width="1.4"><circle cx="12" cy="8" r="4.5"/><path d="M3.5 21c0-4.5 3.8-7.5 8.5-7.5s8.5 3 8.5 7.5z"/></svg></div>
    <h2>Promotion</h2>
    <p>Bacon ipsum dolor sit amet boudin ribeye flank, beef jowl doner tri-tip.</p>
    <span class="btn">Learn more</span>
  </div>
  <div class="block feature" style="top:561px">
    <div class="icon"><svg width="24" height="24" viewBox="0 0 24 24" fill="none" stroke="#3a3a3a" stroke-width="1.4"><rect x="4.5" y="8" width="15" height="13" rx="1"/><path d="M8.5 10V6.5a3.5 3.5 0 0 1 7 0V10"/></svg></div>
    <h2>News or events</h2>
    <p>Bacon ipsum dolor sit amet boudin ribeye flank, beef jowl doner tri-tip.</p>
    <span class="btn">Learn more</span>
  </div>
  <div class="block feature" style="top:770px">
    <div class="icon"><svg width="24" height="24" viewBox="0 0 24 24" fill="none" stroke="#3a3a3a" stroke-width="1.4"><rect x="4" y="3" width="13" height="18" rx="1"/><circle cx="10.5" cy="10" r="2.5"/><path d="M6.5 17c.5-2.5 2-3.5 4-3.5s3.5 1 4 3.5M19.5 7v12"/></svg></div>
    <h2>Or key features</h2>
    <p>Bacon ipsum dolor sit amet boudin ribeye flank, beef jowl doner tri-tip.</p>
    <span class="btn">Learn more</span>
  </div>
  <div class="photo" style="top:988px;left:22px;width:186px;height:144px;background:linear-gradient(180deg,#2d2d2f,#f1f1f1 8%,#e8e8e8 92%,#b9b9bb)" role="img" aria-label="Laptop showing the website"></div>
  <div class="block" style="top:1190px"><h2>Area for picture stories...</h2></div>
</section>

<!-- Column 2 -->
<section class="column col-2">
  <div class="photo" style="top:0;left:40px;width:150px;height:5px;background:#c9c9cb" role="img" aria-label="Laptop base"></div>
  <div class="block" style="top:46px">
    <h2 style="margin-bottom:8px">Area for picture stories....</h2>
    <p>Bacon ipsum dolor sit amet chuck hamburger ribeye sirloin, meatloaf ball tip filet mignon pancetta shank. Tail turkey pork, ribeye sirloin tenderloin jerky beef bacon flank. Tenderloin strip steak ham bacon short loin leberkas</p>
    <span class="read-more">Read more</span>
  </div>
  <div class="block feature" style="top:210px">
    <div class="icon"><svg width="24" height="24" viewBox="0 0 24 24" fill="none" stroke="#3a3a3a" stroke-width="1.4"><rect x="4" y="3" width="13" height="18" rx="1"/><circle cx="10.5" cy="10" r="2.5"/><path d="M6.5 17c.5-2.5 2-3.5 4-3.5s3.5 1 4 3.5M19.5 7v12"/></svg></div>
    <h2>More space</h2>
    <p>Bacon ipsum dolor sit amet boudin ribeye flank, beef jowl doner tri-tip.</p>
    <span class="btn">Learn more</span>
  </div>
  <div class="block feature" style="top:419px">
    <div class="icon"><svg width="24" height="24" viewBox="0 0 24 24" fill="none" stroke="#3a3a3a" stroke-width="1.4"><circle cx="12" cy="8" r="4.5"/><path d="M3.5 21c0-4.5 3.8-7.5 8.5-7.5s8.5 3 8.5 7.5z"/></svg></div>
    <h2>More space</h2>
    <p>Bacon ipsum dolor sit amet boudin ribeye flank, beef jowl doner tri-tip.</p>
    <span class="btn">Learn more</span>
  </div>
  <div class="block white-panel" style="top:638px;height:268px;padding-top:36px">
    <h2 style="font-weight:600;color:var(--navy);font-size:10px">Awesome responsive design</h2>
    <div style="margin:12px auto 0;width:206px;height:84px;background:linear-gradient(90deg,#d9b26a,#6b7f95 45%,#a5573b 60%,#8aa0a8)" role="img" aria-label="Row of monitors displaying terrain modelling software"></div>
    <p style="margin-top:14px;font-size:8px">This is a hero or feature story area.</p>
    <div style="margin-top:14px"><span class="btn">Learn more</span></div>
  </div>
  <div class="block" style="top:944px">
    <h2 style="margin-bottom:8px">Text area</h2>
    <p>Bacon ipsum dolor sit amet chuck hamburger ribeye sirloin, meatloaf ball tip filet mignon pancetta shank. Tail turkey pork, ribeye sirloin tenderloin jerky beef bacon flank. Tenderloin strip steak ham bacon short loin leberkas swine. On ipsum dolor sit amet chuck hamburger ribeye sirloin, meatloaf ball tip filet mignon pancetta shank. Tail turkey pork, ribeye sirloin tenderloin jerky beef bacon flank. Tenderloin strip steak ham bacon short loin leberkas swine</p>
    <span class="read-more">Read more</span>
  </div>
  <div class="block" style="top:1168px"><h2>Area for picture stories....</h2></div>
</section>

<!-- Column 3 -->
<section class="column col-3">
  <div class="block white-panel" style="top:0;height:44px"></div>
  <div class="block" style="top:84px">
    <h2 style="margin-bottom:8px">Text area</h2>
    <p>Bacon ipsum dolor sit amet chuck hamburger ribeye sirloin, meatloaf ball tip filet mignon pancetta shank. Tail turkey pork, ribeye sirloin tenderloin jerky beef bacon flank. Tenderloin strip steak ham bacon short loin leberkas swine. On ipsum dolor sit amet chuck hamburger ribeye sirloin, meatloaf ball tip filet mignon pancetta shank. Tail turkey pork, ribeye sirloin tenderloin jerky beef bacon flank. Tenderloin strip steak ham bacon short loin leberkas swine</p>
    <span class="read-more">Read more</span>
  </div>
  <div class="block" style="top:306px">
    <h2 style="margin-bottom:8px">Area for picture stories....</h2>
    <p>Bacon ipsum dolor sit amet chuck hamburger ribeye sirloin, meatloaf ball tip filet mignon pancetta shank. Tenderloin strip steak ham bacon short loin leberkas</p>
    <span class="read-more">Read more</span>
  </div>
  <div class="photo" style="top:436px;left:40px;width:160px;height:181px;background:linear-gradient(180deg,#1f1f1f,#f2f2f2 12%,#e6e6e6)" role="img" aria-label="Tablet and phone showing the brand app"></div>
  <div class="block dark-panel" style="top:617px;height:446px;padding-top:22px">
    <h2 style="margin-bottom:14px">Gallery</h2>
    <p style="color:var(--white)">Bacon ipsum dolor sit amet chuck hamburger ribeye sirloin, meatloaf ball tip filet mignon pancetta shank.</p>
    <div class="photo" style="top:112px;left:28px;width:82px;height:300px" role="img" aria-label="Surveyor at a construction site"></div>
    <div class="photo" style="top:112px;left:121px;width:82px;height:300px;background:linear-gradient(160deg,#d89a35,#6e5432)" role="img" aria-label="Excavator and machine control screen"></div>
  </div>
  <div class="block white-panel subscribe" style="top:1063px;height:137px;padding-top:30px">
    <h2 style="margin-bottom:12px">Subscribe to our newsletter</h2>
    <p style="font-size:8px;line-height:15px">This Email address field is a trigger with a link that goes to your website when clicked on it. You can't type your email address for real. Alternatively, you can set it as a Mailto function.</p>
  </div>
</section>

<!-- Column 4 -->
<section class="column col-4">
  <div class="block" style="top:0;height:113px;background:var(--stage)">
    <div class="photo" style="top:0;left:28px;width:82px;height:78px" role="img" aria-label="Surveyor at a construction site"></div>
    <div class="photo" style="top:0;left:121px;width:82px;height:78px;background:linear-gradient(160deg,#d89a35,#6e5432)" role="img" aria-label="Machine control screen in a cab"></div>
  </div>
  <div class="block white-panel subscribe" style="top:113px;height:199px;padding-top:24px">
    <h2 style="margin-bottom:14px">Subscribe to our newsletter</h2>
    <p style="font-size:8px;line-height:15px;padding:0 12px">This Email address field is a trigger with a link that goes to your website when clicked on it. You can't type your email address for real. Alternatively, you can set it as a Mailto function.</p>
    <div class="subscribe-form" style="margin-top:18px"><span class="field">Enter your Email address...</span><span class="submit">NOTIFY ME</span></div>
  </div>
  <div class="block" style="top:350px">
    <h2 style="margin-bottom:8px">Text area</h2>
    <p>Bacon ipsum dolor sit amet chuck hamburger ribeye sirloin, meatloaf ball tip filet mignon pancetta shank. Tail turkey pork, ribeye sirloin tenderloin jerky beef bacon flank. Tenderloin strip steak ham bacon short loin leberkas swine. On ipsum dolor sit amet chuck hamburger ribeye sirloin, meatloaf ball tip filet mignon pancetta shank. Tail turkey pork, ribeye sirloin tenderloin jerky beef bacon flank. Tenderloin strip steak ham bacon short loin leberkas swine</p>
    <span class="read-more">Read more</span>
  </div>
  <div class="video-card" style="top:586px;height:295px;padding-top:30px">
    <h2>Space to insert video</h2>
    <div style="position:relative;margin:14px auto 0;width:166px;height:110px;background:linear-gradient(180deg,#f4f4f4,#e2e2e2);border:1px solid #ddd;display:flex;align-items:center;justify-content:center" role="img" aria-label="Video player preview on a laptop">
      <svg width="44" height="44" viewBox="0 0 44 44"><circle cx="22" cy="22" r="19" fill="#555" stroke="#fff" stroke-width="2.5"/><path d="M18 13l12 9-12 9z" fill="#fff"/></svg>
    </div>
    <p style="margin-top:16px;padding:0 14px">Lorem ipsum dolor sit amet, consectetur adipisicing elit, sed do eiusmod tempor incididunt ut labore et dolore magna aliqua.</p>
    <div style="margin-top:14px"><span class="btn">Learn more</span></div>
  </div>
  <footer class="block footer" style="top:915px;height:285px;padding-top:34px">
    <div class="tagline" style="margin-top:18px">We hope you love it as<br>much as we do!</div>
    <div class="rule" style="margin:28px 0 20px"></div>
    <div class="socials"><span class="social"></span><span class="social"></span><span class="social"></span><span class="social"></span><span class="social"></span><span class="social"></span></div>
    <small style="display:block;margin-top:36px">Copyright © 2014 Northlane Studio</small>
    <div class="footer-links" style="margin-top:26px"><span>Unsubscribe</span><span>Privacy</span><span>info@northlane.example</span></div>
  </footer>
</section>

</body>
</html>
```